Talvin Foundation Letterhead

We are a newly established non profit registered in Maryland but operates in Africa, south of the sahara. We offer scholarships to deserving young adults from high school through college. Our color theme for our existing logo is purple, we want a design that is stylish, spellbinding yet a letterhead that projects seriousness. More information on www.thetalvinfoundation.example

Target Market(s)

High school and college students in sub saharan African as well as our donors in the US

Industry/Entity Type

Non Profit

Font styles to use
Script

Requirements
Must have
• Logo at the top and if possible watermark the logo in the middle of the letterhead, contact address,
Should not have
• NA

```html
<!DOCTYPE html>
<html lang="en">
<head>
<meta charset="utf-8">
<title>Talvin Foundation Letterhead</title>
<link rel="stylesheet" href="https://fonts.googleapis.com/css2?family=Cinzel:wght@600&family=Lato:wght@400;700&display=swap">
<style>
  :root {
    --backdrop: #ece8ef;
    --paper: #ffffff;
    --purple: #5b2d8e;
    --purple-light: #8a6bb8;
    --lilac-faint: #ede8f4;
    --ink: #1f1f24;
    --muted: #555560;
    --signature-tone: #d9d6de;
  }
  * { box-sizing: border-box; margin: 0; padding: 0; }
  html, body {
    width: 1112px; height: 1200px; overflow: hidden;
    background: var(--backdrop);
  }
  .letterhead {
    position: absolute; left: 196px; top: 88px;
    width: 708px; height: 1000px;
    background: var(--paper);
    box-shadow: 0 2px 10px rgba(0,0,0,.08);
    font-family: "Lato", sans-serif; color: var(--ink);
    overflow: hidden;
  }
  .brand-mark {
    position: absolute; left: 0; right: 0; top: 46px;
    display: flex; flex-direction: column; align-items: center;
  }
  .brand-circle {
    width: 82px; height: 82px; border-radius: 50%;
    border: 4px solid var(--purple-light);
  }
  .brand-name {
    margin-top: 22px;
    font-family: "Lato", sans-serif; font-weight: 400;
    font-size: 18px; letter-spacing: .5px; color: var(--purple);
  }
  .watermark {
    position: absolute; left: 159px; top: 372px;
    width: 420px; height: 420px; border-radius: 50%;
    border: 14px solid var(--lilac-faint);
  }
  .letter {
    position: absolute; left: 35px; top: 228px; width: 637px;
    font-size: 14px; line-height: 19px;
  }
  .letter-date { margin-bottom: 19px; }
  .recipient { margin-bottom: 26px; font-style: normal; }
  .salutation { margin-bottom: 17px; }
  .letter-body p { margin-bottom: 19px; text-align: justify; }
  .closing {
    position: absolute; left: 35px; top: 754px;
    font-size: 14px; line-height: 18px; color: var(--muted);
  }
  .signature {
    width: 120px; height: 46px; margin: 14px 0 10px;
    background: var(--signature-tone); border-radius: 4px;
  }
  .contact {
    position: absolute; left: 32px; top: 910px;
    font-size: 14px; line-height: 19px; color: var(--ink);
  }
  .contact-name {
    font-family: "Cinzel", serif; font-weight: 600;
    font-size: 16px; color: var(--purple); letter-spacing: .4px;
  }
  .contact-label { color: var(--purple); font-weight: 700; }
  .footer-mark {
    position: absolute; right: 26px; top: 912px;
    width: 44px; height: 44px; border-radius: 50%;
    border: 4px solid var(--purple-light);
  }
  .footer-band {
    position: absolute; left: 0; right: 0; bottom: 0; height: 26px;
  }
</style>
</head>
<body>
  <main class="letterhead">
    <header class="brand-mark">
      <div class="brand-circle"></div>
      <div class="brand-name">Talvin Foundation</div>
    </header>

    <div class="watermark" aria-hidden="true"></div>

    <article class="letter">
      <p class="letter-date">January 12, 2014</p>
      <address class="recipient">
        Mr. John Doe<br>President<br>AA Corporation<br>111 Street Name, Suite#<br>City, State, 12345
      </address>
      <p class="salutation">Dear Mr. John,</p>
      <div class="letter-body">
        <p>Lorem Ipsum is simply dummy text of the printing and typesetting industry. Lorem Ipsum has been the industry's standard dummy text ever since the 1500s, when an unknown printer took a galley of type and scrambled it to make a type specimen book. It has survived not only five centuries, but also the leap into electronic typesetting, remaining essentially unchanged.</p>
        <p>The standard chunk of Lorem Ipsum used since the 1500s is reproduced below for those interested. Sections 1.10.32 and 1.10.33 from "de Finibus Bonorum et Malorum" by Cicero are also reproduced in their exact original form, accompanied by English versions from the 1914 translation by H. Rackham</p>
        <p>Lorem Ipsum is simply dummy text of the printing and typesetting industry. Lorem Ipsum has been the industry's standard dummy text ever since the 1500s, when an unknown printer took a galley of type and scrambled it to make a type specimen book. It has survived not only five centuries, but also the leap into electronic typesetting, remaining essentially unchanged. It was popularised in the</p>
      </div>
    </article>

    <section class="closing">
      <p>Sincerely Your,</p>
      <div class="signature" role="img" aria-label="Handwritten signature"></div>
      <p>Name Last Name<br>Company Name</p>
    </section>

    <footer class="contact">
      <p class="contact-name">The Talvin Foundation Inc</p>
      <p>18 Willow Crest Lane, Suite 2, Ellicott City, MD 21043</p>
      <p><span class="contact-label">E</span>: admin@thetalvinfoundation.example <span class="contact-label">W</span>: www.thetalvinfoundation.example</p>
    </footer>
    <div class="footer-mark" aria-hidden="true"></div>

    <svg class="footer-band" viewBox="0 0 708 26" preserveAspectRatio="none" aria-hidden="true">
      <rect x="0" y="0" width="708" height="3" fill="var(--purple-light)"/>
      <rect x="0" y="7" width="708" height="19" fill="var(--purple)"/>
    </svg>
  </main>
</body>
</html>
```